TallyForge needs a new rocket based website

We need a new website that will be based on our rocket ship logo. We develop innovative solutions for enterprises. We would like to see a design that when the pages scroll, the rocket launches and goes from launch through a journey, similar to how we approach our customer. We would like areas for "Who are we", "What can we do", "What have we done", "How can we help". http://www.tallyforge.com.au is our current website

Target Market(s)

Government, Enterprise, Cloud

Industry/Entity Type

Software Service

Coding

Coded - Design and coding required

Number of Pages Required

2 page

Requirements
Must have
• We would like to see a design that when the pages scroll, the rocket launches and goes from launch through a journey, similar to how we approach our customer.
• Must have a home page and a detail page.
• Would like to see the logo/rocket animate in some way when you scroll through he page.

```html
<!DOCTYPE html>
<html lang="en">
<head>
<meta charset="utf-8">
<title>TallyForge — Innovative Software Solutions</title>
<link rel="stylesheet" href="https://fonts.googleapis.com/css2?family=Michroma&family=Nunito+Sans:wght@400;600;700;800&display=swap">
<style>
  :root {
    --orange: #f7931e;
    --hero-light: #f2a24e;
    --hero-mid: #d9772a;
    --hero-dark: #8a3f12;
    --light: #f1f1f1;
    --white: #ffffff;
    --field: #f2f2f2;
    --ink: #4a4a4a;
    --heading: #2e2e2e;
    --dark: #3b3b3b;
    --map-a: #ebe9e4;
    --map-b: #dfe3da;
    --link-blue: #4a84d4;
  }
  * { box-sizing: border-box; margin: 0; padding: 0; }
  html, body { width: 1200px; height: 2857px; overflow: hidden; }
  body {
    position: relative;
    background: var(--white);
    font-family: "Nunito Sans", Arial, sans-serif;
    color: var(--ink);
  }
  .display { font-family: "Michroma", "Arial Black", sans-serif; }

  /* Hero */
  .hero { position: absolute; left: 0; top: 0; width: 1200px; height: 800px; }
  .hero-art { position: absolute; inset: 0; }
  .brand {
    position: absolute; left: 46px; top: 60px;
    display: flex; align-items: center; gap: 10px;
    color: var(--white); font-size: 30px; font-weight: 800; letter-spacing: -0.5px;
  }
  .brand-dot { width: 14px; height: 14px; border-radius: 50%; background: var(--white); }
  .main-nav { position: absolute; right: 30px; top: 80px; display: flex; gap: 28px; }
  .main-nav a { color: var(--white); text-decoration: none; font-size: 13px; }
  .hero-title {
    position: absolute; left: 95px; top: 360px;
    color: var(--white); font-size: 33px; font-weight: 800; line-height: 42px;
  }

  /* Section headings */
  .section-title {
    position: absolute; left: 0; width: 1200px;
    display: flex; justify-content: center; align-items: center; gap: 18px;
    font-size: 27px; font-weight: 400; color: var(--heading);
  }
  .section-title .mark { width: 16px; height: 16px; border-radius: 50%; background: var(--orange); }
  .section-title em { font-style: normal; color: var(--orange); }

  /* Who we are */
  .who { position: absolute; left: 0; top: 790px; width: 1200px; height: 620px; background: var(--light); }
  .who .section-title { top: 108px; }
  .who-photo {
    position: absolute; left: 91px; top: 202px; width: 482px; height: 300px;
    background: var(--white); border-radius: 30px; padding: 14px;
    box-shadow: 0 2px 8px rgba(0,0,0,0.12);
  }
  .who-photo-fill {
    width: 100%; height: 100%; border-radius: 20px;
    background:
      radial-gradient(circle at 75% 30%, rgba(255,255,255,0.8), rgba(255,255,255,0) 45%),
      linear-gradient(135deg, #5e7288 0%, #a9bccd 45%, #e9eef3 100%);
  }
  .who-copy { position: absolute; left: 638px; top: 196px; width: 462px; font-size: 22px; line-height: 29px; letter-spacing: -0.2px; }
  .who-copy p + p { margin-top: 29px; }

  /* Contact */
  .help { position: absolute; left: 0; top: 1410px; width: 1200px; height: 547px; background: var(--white); }
  .help .section-title { top: 110px; }
  .field {
    position: absolute; background: var(--field); border-radius: 3px;
    font-size: 16px; font-weight: 700; color: var(--heading); padding: 12px 16px;
  }
  .send {
    position: absolute; left: 480px; top: 409px; width: 240px; height: 44px;
    background: var(--orange); border-radius: 22px; color: var(--white);
    font-size: 21px; font-weight: 700; display: flex; align-items: center; justify-content: center;
  }

  /* Map */
  .map { position: absolute; left: 0; top: 1957px; width: 1200px; height: 440px;
    background:
      radial-gradient(ellipse at 92% 20%, rgba(196,226,186,0.7), rgba(196,226,186,0) 18%),
      radial-gradient(ellipse at 55% 40%, rgba(250,240,222,0.9), rgba(250,240,222,0) 30%),
      linear-gradient(180deg, var(--map-a) 0%, var(--map-b) 100%); }
  .map-card {
    position: absolute; left: 17px; top: 1963px; width: 316px; height: 84px;
    background: var(--white); box-shadow: 0 1px 4px rgba(0,0,0,0.25);
    padding: 9px 10px; font-size: 11px; color: var(--heading);
  }
  .map-card strong { display: block; font-size: 13px; font-weight: 700; }
  .map-card .addr { color: #555; margin-top: 3px; }
  .map-card .more { position: absolute; left: 10px; bottom: 8px; color: var(--link-blue); }
  .map-actions { position: absolute; right: 14px; top: 10px; display: flex; gap: 18px; color: var(--link-blue); font-size: 11px; text-align: center; }
  .map-actions i { display: block; width: 14px; height: 14px; margin: 0 auto 4px; background: var(--link-blue); border-radius: 2px; }

  /* Footer */
  .footer-edge { position: absolute; left: 0; top: 2260px; width: 1200px; height: 140px; }
  .footer { position: absolute; left: 0; top: 2398px; width: 1200px; height: 406px; background: var(--dark); color: var(--white); }
  .footer-brand {
    position: absolute; left: 0; width: 1200px; top: 50px;
    display: flex; justify-content: center; align-items: center; gap: 10px;
    font-size: 38px; font-weight: 800; letter-spacing: -0.5px;
  }
  .footer-brand .brand-dot { width: 16px; height: 16px; }
  .footer-col { position: absolute; top: 160px; font-size: 15px; }
  .footer-col h3 {
    font-size: 15px; font-weight: 800; text-transform: uppercase;
    padding-bottom: 10px; border-bottom: 1px solid #9a9a9a; margin-bottom: 16px;
  }
  .links { width: 157px; left: 177px; list-style: none; }
  .links li { line-height: 23px; font-weight: 600; white-space: nowrap; }
  .links li::before { content: "▸ "; font-size: 12px; }
  .contact { left: 455px; width: 192px; }
  .contact-row { display: flex; gap: 8px; font-weight: 600; line-height: 18px; margin-bottom: 22px; white-space: nowrap; }
  .contact-row svg { flex: none; margin-top: 1px; }
  .newsletter { left: 768px; width: 256px; }
  .newsletter p { font-weight: 600; line-height: 18px; margin-bottom: 10px; }
  .email-field { height: 31px; background: var(--white); border-radius: 15px; color: var(--heading);
    font-weight: 600; padding: 6px 20px; margin-bottom: 12px; }
  .subscribe { width: 128px; height: 31px; border-radius: 15px; background: var(--orange);
    font-weight: 800; font-size: 13px; display: flex; align-items: center; justify-content: center; }
  .legal {
    position: absolute; left: 0; top: 2804px; width: 1200px; height: 53px; background: var(--orange);
    color: var(--white); font-size: 13px; font-weight: 800; padding: 0 30px;
    display: flex; align-items: center; justify-content: space-between;
  }
  .social { display: flex; gap: 10px; }
  .social span { width: 20px; height: 20px; border-radius: 50%; background: var(--white); }
</style>
</head>
<body>

<header class="hero">
  <svg class="hero-art" width="1200" height="800" viewBox="0 0 1200 800">
    <defs>
      <linearGradient id="heroBase" x1="0" y1="0" x2="1" y2="1">
        <stop offset="0" stop-color="var(--hero-mid)"/>
        <stop offset="0.55" stop-color="#c8621d"/>
        <stop offset="1" stop-color="var(--hero-dark)"/>
      </linearGradient>
      <radialGradient id="glowRight" cx="0.68" cy="0.22" r="0.35">
        <stop offset="0" stop-color="var(--hero-light)" stop-opacity="0.95"/>
        <stop offset="1" stop-color="var(--hero-light)" stop-opacity="0"/>
      </radialGradient>
      <radialGradient id="glowLeft" cx="0.18" cy="0.35" r="0.3">
        <stop offset="0" stop-color="#f0a055" stop-opacity="0.6"/>
        <stop offset="1" stop-color="#f0a055" stop-opacity="0"/>
      </radialGradient>
      <radialGradient id="shadeLow" cx="0.35" cy="0.85" r="0.3">
        <stop offset="0" stop-color="#7a3510" stop-opacity="0.55"/>
        <stop offset="1" stop-color="#7a3510" stop-opacity="0"/>
      </radialGradient>
    </defs>
    <rect width="1200" height="800" fill="var(--light)"/>
    <polygon points="0,670 600,778 1200,670 1200,692 600,790 0,692" fill="var(--orange)"/>
    <g role="img" aria-label="Photo of a hand turning glowing orange gears">
      <polygon points="0,0 1200,0 1200,680 600,765 0,680" fill="url(#heroBase)"/>
      <polygon points="0,0 1200,0 1200,680 600,765 0,680" fill="url(#glowRight)"/>
      <polygon points="0,0 1200,0 1200,680 600,765 0,680" fill="url(#glowLeft)"/>
      <polygon points="0,0 1200,0 1200,680 600,765 0,680" fill="url(#shadeLow)"/>
    </g>
  </svg>
  <div class="brand"><span class="brand-dot"></span>TallyForge</div>
  <nav class="main-nav display">
    <a href="#who">Who Are We</a>
    <a href="#what">What Can We Do</a>
    <a href="#done">What Have We Done</a>
    <a href="#help">How Can We Help</a>
  </nav>
  <h1 class="hero-title">TallyForge offers highly<br>innovative software solutions</h1>
</header>

<section class="who" id="who">
  <h2 class="section-title display"><span class="mark"></span>Who <em>We Are</em></h2>
  <div class="who-photo">
    <div class="who-photo-fill" role="img" aria-label="Photo of a hand tapping a tablet with floating chart graphics"></div>
  </div>
  <div class="who-copy">
    <p>Lorem ipsum dolor sit amet, consectetur adi piscing elit, sed do eiusmod tempor incidid unt ut labore et dolore magna aliqua. Ut eni ad minim veniam, quis nostrud exercitation ullaco laboris nisi ut aliquip ex ea commodo consequat.</p>
    <p>Duis aute irure dolor in reprehenderit in vol uptate velit esse cillum dolore eu fugiat nulla pariatur. Excepteur sint occaecat cupidatat non proident, sunt in culpa qui officia.</p>
  </div>
</section>

<section class="help" id="help">
  <h2 class="section-title display"><span class="mark"></span>How Can We Help</h2>
  <div class="field" style="left:116px;top:202px;width:313px;height:45px;">Your Name</div>
  <div class="field" style="left:444px;top:202px;width:312px;height:45px;">Your Email</div>
  <div class="field" style="left:771px;top:202px;width:313px;height:45px;">Your Subject</div>
  <div class="field" style="left:116px;top:263px;width:968px;height:131px;">Message</div>
  <div class="send">Send</div>
</section>

<div class="map" role="img" aria-label="Street map showing the office location"></div>
<div class="map-card">
  <strong>7/48 Harlow Rd</strong>
  <div class="addr">48 Harlow Rd, Kensworth SA 5071</div>
  <div class="map-actions">
    <span><i></i>Directions</span>
    <span><i></i>Save</span>
  </div>
  <span class="more">View larger map</span>
</div>

<svg class="footer-edge" width="1200" height="140" viewBox="0 0 1200 140">
  <polygon points="0,8 600,100 1200,8 1200,140 0,140" fill="var(--dark)"/>
  <polygon points="0,24 600,108 1200,24 1200,33 600,124 0,33" fill="var(--orange)"/>
</svg>

<footer class="footer">
  <div class="footer-brand"><span class="brand-dot"></span>TallyForge</div>

  <ul class="footer-col links">
    <h3>Quick Links</h3>
    <li>Who We Are</li>
    <li>What Can We Do</li>
    <li>What Have We Done</li>
    <li>How Can We Help</li>
  </ul>

  <div class="footer-col contact">
    <h3>Contact</h3>
    <div class="contact-row">
      <svg width="16" height="16" viewBox="0 0 16 16"><circle cx="8" cy="8" r="7" fill="none" stroke="var(--orange)" stroke-width="1.5"/><path d="M8 4a2.5 2.5 0 0 0-2.5 2.5C5.5 9 8 12 8 12s2.5-3 2.5-5.5A2.5 2.5 0 0 0 8 4z" fill="var(--orange)"/></svg>
      <span>TallyForge<br>Unit 7, 48 Harlow Rd<br>Kensworth, SA 5071</span>
    </div>
    <div class="contact-row">
      <svg width="16" height="16" viewBox="0 0 16 16"><circle cx="8" cy="8" r="7" fill="none" stroke="var(--orange)" stroke-width="1.5"/><path d="M5.5 4.5l1.5 0 .7 2-1 .8a5 5 0 0 0 2 2l.8-1 2 .7v1.5c-3.5.5-6.5-2.5-6-6z" fill="var(--orange)"/></svg>
      <span>1300 482 117</span>
    </div>
    <div class="contact-row">
      <svg width="16" height="16" viewBox="0 0 16 16"><circle cx="8" cy="8" r="7" fill="none" stroke="var(--orange)" stroke-width="1.5"/><rect x="4.5" y="5.5" width="7" height="5" fill="none" stroke="var(--orange)" stroke-width="1.2"/><path d="M4.5 5.5L8 8.3l3.5-2.8" fill="none" stroke="var(--orange)" stroke-width="1.2"/></svg>
      <span>info@tallyforge.com.au</span>
    </div>
  </div>

  <div class="footer-col newsletter">
    <h3>Newsletter Subscription</h3>
    <p>Register your email address to get more information about us</p>
    <div class="email-field">Email Address</div>
    <div class="subscribe">SUBSCRIBE</div>
  </div>
</footer>

<div class="legal">
  <span>COPYRIGHT © 2018 TALLYFORGE. ALL RIGHTS RESERVED.</span>
  <div class="social" aria-label="Social links">
    <span></span><span></span><span></span><span></span><span></span>
  </div>
</div>

</body>
</html>
```